Real Estate Company Business Cards
Renaming and Rebranding existing real estate company
Real Estate Company Business Cards - Real Estate
Creative Brief
Professional
Desmond (Hal) Pruitt, Jr
Broker, Realtor, SPS, E-Pro, BPOR,
482 Willow Bend Rd. St 23 Orange Park, Florida 32068
NC Office 910-555-0187
Fl Office 904-555-0162
hpruitt@pruittrealty.example
www.pruittrealty.example
Please dont include address in card design. These card will be printed on cotton or silk.

```html
<!DOCTYPE html>
<html lang="en">
<head>
<meta charset="utf-8">
<title>Pruitt Realty Stationery</title>
<link href="https://fonts.googleapis.com/css2?family=Libre+Baskerville:wght@700&family=Open+Sans:wght@400;600&display=swap" rel="stylesheet">
<style>
:root{
  --navy:#1d3a6b;
  --blue:#2c64a8;
  --blue-light:#4a86c8;
  --grey:#9aa3ad;
  --line:#c9ced4;
  --paper:#ffffff;
  --bg:#ffffff;
  --faint:#e9edf2;
  --shadow:0 2px 6px rgba(0,0,0,.18);
}
*{margin:0;padding:0;box-sizing:border-box}
html,body{width:1200px;height:936px;overflow:hidden;background:var(--bg)}
.canvas{position:relative;width:1200px;height:936px;font-family:"Open Sans",Arial,sans-serif}
.sheet{position:absolute;background:var(--paper);box-shadow:var(--shadow);overflow:hidden}
.brand{display:flex;align-items:center;gap:6px;color:var(--navy);font-family:"Libre Baskerville",Georgia,serif;font-weight:700;line-height:1.05}
.brand > span:last-child{white-space:nowrap}
.brand-dot{border-radius:50%;background:var(--navy);flex:none}
.footer-band{position:absolute;right:0;background:linear-gradient(90deg,var(--navy),var(--blue-light));clip-path:polygon(14px 0,100% 0,100% 100%,0 100%);color:#fff;font-size:9px;letter-spacing:2px;display:flex;align-items:center;padding-left:26px;white-space:nowrap}
.footer-line{position:absolute;left:0;height:2px;background:var(--line)}

/* letterhead */
.letterhead{left:140px;top:71px;width:317px;height:551px}
.letterhead .brand{position:absolute;left:20px;top:20px;font-size:9px}
.letterhead .brand-dot{width:22px;height:22px}
.contact-list{position:absolute;right:14px;top:16px;font-size:5.5px;color:#555;line-height:9px}
.contact-list li{list-style:none;display:flex;align-items:center;gap:3px;white-space:nowrap}
.contact-list i{width:5px;height:5px;background:var(--navy);border-radius:50%;display:inline-block}
.watermark{position:absolute;left:88px;top:124px;width:150px;height:150px;border-radius:50%;background:var(--faint)}
.letterhead .footer-band{bottom:18px;width:200px;height:16px;font-size:7px;letter-spacing:1.5px;padding-left:22px}
.letterhead .footer-line{bottom:25px;width:140px}

/* folder */
.folder{left:634px;top:56px;width:482px;height:566px}
.folder .brand{position:absolute;left:100px;top:168px;font-size:26px}
.folder .brand-dot{width:60px;height:60px}
.folder .brand small{display:block;font-size:15px;color:var(--blue)}
.folder .footer-band{bottom:18px;width:230px;height:20px}
.folder .footer-line{bottom:27px;width:270px}

/* cards */
.card{left:20px;width:234px;height:104px}
.card-front{top:657px}
.card-back{top:781px}
.card-front .brand{position:absolute;left:10px;top:10px;font-size:9px}
.card-front .brand-dot{width:20px;height:20px}
.card-front .contact-list{top:50px;left:10px;right:auto;font-size:5px;line-height:8px}
.card-person{position:absolute;right:12px;top:52px;text-align:right;font-size:6px;color:var(--navy);font-weight:600;white-space:nowrap}
.card-person span{display:block;font-weight:400;color:#666;font-size:5px}
.card-front .footer-band{bottom:0;width:234px;height:6px;clip-path:none;padding:0}
.card-back .brand{position:absolute;left:50%;top:50%;transform:translate(-50%,-50%);font-size:12px}
.card-back .brand-dot{width:30px;height:30px}

/* envelopes */
.envelope-front{left:292px;top:665px;width:286px;height:190px}
.envelope-front .brand{position:absolute;left:12px;top:12px;font-size:9px}
.envelope-front .brand-dot{width:20px;height:20px}
.envelope-back{left:609px;top:665px;width:563px;height:190px}
.envelope-back svg{position:absolute;inset:0}
.flap-url{position:absolute;left:0;right:0;top:28px;text-align:center;color:#fff;font-size:9px;letter-spacing:2px}
</style>
</head>
<body>
<div class="canvas">

  <section class="sheet letterhead">
    <div class="brand"><span class="brand-dot"></span><span>Pruitt Realty<br>and Property<br>Management Services</span></div>
    <ul class="contact-list">
      <li><i></i>910-555-0187</li>
      <li><i></i>904-555-0162</li>
      <li><i></i>hpruitt@pruittrealty.example</li>
      <li><i></i>www.pruittrealty.example</li>
    </ul>
    <div class="watermark"></div>
    <div class="footer-line"></div>
    <div class="footer-band">www.pruittrealty.example</div>
  </section>

  <section class="sheet folder">
    <div class="brand"><span class="brand-dot"></span><span>Pruitt Realty<small>and Property<br>Management Services</small></span></div>
    <div class="footer-line"></div>
    <div class="footer-band">www.pruittrealty.example</div>
  </section>

  <section class="sheet card card-front">
    <div class="brand"><span class="brand-dot"></span><span>Pruitt Realty<br>and Property<br>Management Services</span></div>
    <ul class="contact-list">
      <li><i></i>910-555-0187</li>
      <li><i></i>904-555-0162</li>
      <li><i></i>hpruitt@pruittrealty.example</li>
      <li><i></i>www.pruittrealty.example</li>
    </ul>
    <div class="card-person">Desmond (Hal) Pruitt, Jr<span>Broker, Realtor</span></div>
    <div class="footer-band"></div>
  </section>

  <section class="sheet card card-back">
    <div class="brand"><span class="brand-dot"></span><span>Pruitt Realty<br>and Property<br>Management Services</span></div>
  </section>

  <section class="sheet envelope-front">
    <div class="brand"><span class="brand-dot"></span><span>Pruitt Realty<br>and Property<br>Management Services</span></div>
  </section>

  <section class="sheet envelope-back">
    <svg width="563" height="190" viewBox="0 0 563 190">
      <defs>
        <linearGradient id="flapGrad" x1="0" y1="0" x2="0" y2="1">
          <stop offset="0" stop-color="#1d3a6b"/>
          <stop offset="1" stop-color="#3f7cc0"/>
        </linearGradient>
      </defs>
      <path d="M0 190 L250 118 Q281 110 313 118 L563 190" fill="none" stroke="#dfe3e8" stroke-width="1.5"/>
      <path d="M0 0 H563 V30 L320 92 Q281 102 243 92 L0 30 Z" fill="url(#flapGrad)"/>
    </svg>
    <div class="flap-url">www.pruittrealty.example</div>
  </section>

</div>
</body>
</html>
```